Visitenkarten-Design für Fachärztin für Allgemeinmedizin
Zielgruppe
Visitenkarte passend zum Logo mit folgenden Daten:
Dr. med Miriam Valdorf
Fachärztin für Allgemeinmedizin
Brennwaldweg 14
72946 Talbrunn OT Kellingen
Telefon 07451/8194
Website: www.hausarztpraxis-talgrund.de
Online Terminvereinbarung
Sprechstunde
Mo 8-11:30Uhr sowie 14-17 Uhr
Die 8-13 Uhr
Mi 8-13 Uhr
Do 8-11:30uhr sowie 14-18 Uhr
Fr 8- 11:30Uhr
Sowie nach Vereinbarung
Laborzeiten tägl. 7:15 -8 Uhr
Telefonzeiten tägl. 8-11 Uhr , sowie Mo und Fr 14-16 Uhr
Aufgabenstellung
Nach dem Logo, welches hier erstellt wurde Visitenkarten ..
vorher und Rückseite!
Sprechzeiten, Name, Adresse , Tele Fax und Website
In den Farben des Magenta und Grau

```html
<!DOCTYPE html>
<html lang="de">
<head>
<meta charset="utf-8">
<title>Visitenkarte Hausarztpraxis</title>
<link rel="stylesheet" href="https://fonts.googleapis.com/css2?family=Cormorant+SC:wght@500;600&family=Open+Sans:wght@400;600;700&display=swap">
<style>
  :root {
    --magenta: #c2185b;
    --magenta-dark: #a3144c;
    --grey: #4f5558;
    --grey-light: #7a7f82;
    --paper: #ffffff;
    --backdrop: #cfcfcf;
  }
  * { box-sizing: border-box; margin: 0; padding: 0; }
  html, body { width: 1200px; height: 900px; overflow: hidden; }
  body {
    background: radial-gradient(circle at 50% 45%, #e6e6e6, var(--backdrop) 70%, #a9a9a9);
    font-family: "Open Sans", Arial, sans-serif;
    display: flex; flex-direction: column; align-items: center; justify-content: center; gap: 44px;
  }
  .card {
    width: 600px; height: 388px;
    display: flex;
    background: var(--paper);
    box-shadow: 0 10px 28px rgba(0,0,0,.28);
  }
  .card__band {
    width: 40%;
    background: var(--magenta);
    color: var(--paper);
    position: relative;
  }
  .card__body { flex: 1; position: relative; }

  /* Front */
  .band-title {
    font-family: "Cormorant SC", Georgia, serif;
    font-weight: 600; font-size: 24px; letter-spacing: 1px;
    text-align: center; padding-top: 44px;
  }
  .mark {
    display: flex; flex-direction: column; align-items: center; gap: 14px;
    margin-top: 52px;
  }
  .mark__dot { width: 64px; height: 64px; border-radius: 50%; background: var(--paper); }
  .mark__name {
    font-family: "Cormorant SC", Georgia, serif;
    font-weight: 600; font-size: 24px; color: var(--paper);
  }
  .contact { padding: 44px 34px 0 34px; color: var(--grey); }
  .doctor-name {
    font-family: "Cormorant SC", Georgia, serif;
    font-weight: 600; font-size: 24px; color: var(--magenta); line-height: 1.1;
  }
  .doctor-title { font-size: 13px; color: var(--grey-light); margin-top: 2px; }
  .rule { height: 2px; background: var(--magenta); margin: 14px 0 16px; }
  .address { font-size: 15px; line-height: 1.4; }
  .label { font-size: 13px; color: var(--magenta); text-transform: uppercase; letter-spacing: .2px; margin-top: 6px; }
  .line { display: flex; align-items: center; gap: 8px; font-size: 15px; line-height: 1.45; }
  .line svg { width: 14px; height: 14px; fill: var(--magenta); }
  .web { font-size: 15px; margin-top: 2px; }

  /* Back */
  .hours { padding: 34px 22px 0 26px; font-size: 11.5px; line-height: 1.5; }
  .hours__head { font-weight: 700; text-transform: uppercase; font-size: 12px; }
  .hours__note { font-weight: 700; text-transform: uppercase; font-size: 11px; margin-top: 8px; }
  .hours__rule { height: 1px; background: rgba(255,255,255,.85); margin: 12px 0; }
  .hours__strong { font-weight: 700; text-transform: uppercase; font-size: 11px; }
  .brand {
    height: 100%;
    display: flex; flex-direction: column; align-items: center; justify-content: center; gap: 18px;
  }
  .brand__dot { width: 96px; height: 96px; border-radius: 50%; background: var(--magenta); }
  .brand__name {
    font-family: "Cormorant SC", Georgia, serif;
    font-weight: 600; font-size: 30px; color: var(--magenta);
  }
</style>
</head>
<body>

  <section class="card card--front">
    <div class="card__band">
      <h2 class="band-title">Hausarztpraxis</h2>
      <div class="mark">
        <span class="mark__dot"></span>
        <span class="mark__name">Praxis Talgrund</span>
      </div>
    </div>
    <div class="card__body contact">
      <h1 class="doctor-name">Dr. med. Miriam Valdorf</h1>
      <p class="doctor-title">Fachärztin für Allgemeinmedizin</p>
      <div class="rule"></div>
      <p class="address">Brennwaldweg 14<br>72946 Talbrunn OT Kellingen</p>
      <p class="label">Rezepthotline</p>
      <p class="line">
        <svg viewBox="0 0 24 24" aria-hidden="true"><path d="M6.6 10.8a15.1 15.1 0 0 0 6.6 6.6l2.2-2.2a1 1 0 0 1 1-.25 11.4 11.4 0 0 0 3.6.57 1 1 0 0 1 1 1V20a1 1 0 0 1-1 1A17 17 0 0 1 3 4a1 1 0 0 1 1-1h3.5a1 1 0 0 1 1 1c0 1.25.2 2.45.57 3.57a1 1 0 0 1-.25 1z"/></svg>
        07451/8194
      </p>
      <p class="line">
        <svg viewBox="0 0 24 24" aria-hidden="true"><path d="M7 2h10v5H7zM4 8h16a2 2 0 0 1 2 2v8h-4v4H6v-4H2v-8a2 2 0 0 1 2-2zm4 8v4h8v-4z"/></svg>
        07451/8195
      </p>
      <div class="rule"></div>
      <p class="label">Online Terminvereinbarung</p>
      <p class="web">www.hausarztpraxis-talgrund.de</p>
    </div>
  </section>

  <section class="card card--back">
    <div class="card__band hours">
      <p class="hours__head">Sprechstunde</p>
      <p>Mo 8-11:30 Uhr sowie 14-17 Uhr<br>
         Die 8-13 Uhr<br>
         Mi 8-13 Uhr<br>
         Do 8-11:30 Uhr sowie 14-18 Uhr<br>
         Fr 8-11:30 Uhr</p>
      <p class="hours__note">Sowie nach Vereinbarung</p>
      <div class="hours__rule"></div>
      <p class="hours__strong">Laborzeiten tägl. 7:15-8 Uhr</p>
      <div class="hours__rule"></div>
      <p class="hours__strong">Telefonzeiten tägl. 8-11 Uhr,<br>sowie Mo und Fr 14-16 Uhr</p>
    </div>
    <div class="card__body brand">
      <span class="brand__dot"></span>
      <span class="brand__name">Praxis Talgrund</span>
    </div>
  </section>

</body>
</html>
```